Hedge fund needs power point design for marketing pitch

We need a designer to make our power point pitch more aesthetically appealing to potential clients. We will be marketing our hedge fund to high net worth individuals and financial institutions. The ideal design will look professional and project confidence to our potential clients. We have attached a rough outline of what we have completed so far. We have also attached example cover pages for 2 pitch books produced by our competitors.

Target Market(s)

Financial institutions and wealthy investors

Industry/Entity Type

Finance

Requirements
Must have
• must use our logo and current slides. Must look professional

```html
<!DOCTYPE html>
<html lang="en">
<head>
<meta charset="utf-8">
<title>Quellmore Derivatives Fund LP — Pitch Deck</title>
<link rel="stylesheet" href="https://fonts.googleapis.com/css2?family=Tinos:wght@400;700&family=Arimo:wght@400;700&display=swap">
<style>
:root{
  --stage:#8c8c8c;
  --green:#1d6b43;
  --green-dark:#0f4a2c;
  --green-soft:#2f8a5a;
  --light-green:#9bc27a;
  --gold:#c9a23a;
  --ink:#1a1a1a;
  --wordmark:#444444;
  --rule:#cfcfcf;
  --red:#c0392b;
  --pill:#d9d9d9;
}
*{box-sizing:border-box;margin:0;padding:0}
html,body{width:1200px;height:752px;overflow:hidden}
body{background:var(--stage);position:relative;font-family:"Tinos",serif;color:var(--ink)}
.slide{position:absolute;width:254px;height:192px;background:linear-gradient(#ffffff,#eeeeee);box-shadow:2px 4px 8px rgba(0,0,0,.45);overflow:hidden}
.slide-title{position:absolute;left:20px;top:14px;font-size:13px;font-weight:400;letter-spacing:.1px;z-index:2}
.slide-rule{position:absolute;left:20px;right:12px;top:31px;height:1px;background:var(--rule)}
.footer{position:absolute;left:0;right:0;bottom:0;height:12px;background:linear-gradient(var(--green-soft),var(--green-dark))}
.footer::before{content:"";position:absolute;left:22px;top:3px;width:10px;height:5px;background:#bdbdbd}
.footer::after{content:"";position:absolute;right:36px;top:-1px;border-left:5px solid transparent;border-right:5px solid transparent;border-top:5px solid #fff}
.body-text{position:absolute;font-size:5.4px;line-height:1.35;color:var(--ink)}
.photo{position:absolute}
.wordmark{font-family:"Tinos",serif;font-weight:400;color:var(--wordmark);font-size:8px;letter-spacing:0}
/* cover */
.cover{background:linear-gradient(100deg,#cfcfcf,#f4f4f4 45%,#bdbdbd)}
.cover-band{position:absolute;left:0;right:0;top:52px;height:70px;background:linear-gradient(var(--green-soft),var(--green-dark));border-bottom:2px solid var(--gold)}
.cover-brand{position:absolute;left:0;top:52px;width:70px;height:70px;background:#fff;display:flex;align-items:center;justify-content:center}
.cover-text{position:absolute;left:84px;top:66px;color:#fff}
.cover-text h1{font-size:8px;font-weight:400;margin-bottom:6px}
.cover-text p{font-size:5px;line-height:1.3}
/* tables */
.perf-table{position:absolute;left:18px;top:40px;border-collapse:collapse;font-family:"Arimo",sans-serif;font-size:2.6px}
.perf-table th,.perf-table td{padding:.4px 1.4px;text-align:right;border-bottom:.3px solid #ddd}
.perf-table th{font-weight:700}
.perf-table td:first-child,.perf-table th:first-child{text-align:left}
.perf-table .neg{color:var(--red)}
.chart{position:absolute;left:20px;top:34px;width:214px;height:75px}
/* risk */
.risk-row{position:absolute;left:30px;height:22px;width:180px}
.risk-icon{position:absolute;left:0;top:0;width:22px;height:22px;border-radius:50%;background:#5aa532;border:2px solid #dfe9d8}
.risk-note{position:absolute;left:26px;top:3px;width:154px;min-height:16px;background:var(--pill);border-radius:4px;font-size:4.4px;line-height:1.3;padding:3px 5px;display:flex;align-items:center}
/* terms */
.terms{position:absolute;left:24px;top:38px;width:200px;border-collapse:collapse;font-family:"Arimo",sans-serif;font-size:4.2px}
.terms th{background:var(--light-green);color:#fff;text-align:left;padding:1.2px 3px;font-weight:700}
.terms td{padding:1.1px 3px}
.terms tr:nth-child(even) td{background:#e6efdc}
.terms tr:nth-child(odd) td{background:#f3f7ee}
ul.objectives{position:absolute;left:20px;top:58px;width:100px;font-size:5px;line-height:1.35;list-style:none}
ul.objectives li{position:relative;padding-left:6px;margin-bottom:9px}
ul.objectives li::before{content:"";position:absolute;left:0;top:1.5px;width:3px;height:3px;border-radius:50%;background:var(--green-dark)}
</style>
</head>
<body>

<!-- Row 1 -->
<section class="slide cover" style="left:52px;top:60px">
  <div class="cover-band"></div>
  <div class="cover-brand"><span class="wordmark">Quellmore</span></div>
  <div class="cover-text">
    <h1>Quellmore Derivatives Fund LP</h1>
    <p>Confidential<br>April 2016</p>
  </div>
</section>

<section class="slide" style="left:333px;top:60px">
  <h2 class="slide-title">Disclaimer</h2><div class="slide-rule"></div>
  <p class="body-text" style="left:68px;top:51px;font-size:10px">Get legal counsel on this</p>
  <div class="photo" role="img" aria-label="Laptop displaying a legal notice screen" style="left:17px;top:65px;width:125px;height:110px;background:linear-gradient(160deg,#2b2b2b,#1e5a3a 55%,#c8c8c8 85%);border-radius:3px"></div>
  <div class="footer"></div>
</section>

<section class="slide" style="left:614px;top:60px">
  <h2 class="slide-title">Simulated Performance</h2><div class="slide-rule"></div>
  <table class="perf-table">
    <tr><th>period</th><th>mean</th><th>1%</th><th>5%</th><th>10%</th><th>25%</th><th>50%</th><th>75%</th><th>90%</th><th>max</th></tr>
    <tr><td>weekly</td><td>1.9</td><td class="neg">-11.8</td><td class="neg">-6.1</td><td class="neg">-3.9</td><td>0.2</td><td>2.0</td><td>4.1</td><td>7.2</td><td>32.1</td></tr>
    <tr><td>monthly</td><td>8.7</td><td class="neg">-22.4</td><td class="neg">-11.5</td><td class="neg">-6.3</td><td>1.9</td><td>8.1</td><td>15.2</td><td>23.8</td><td>88.4</td></tr>
    <tr><td>quarterly</td><td>26.4</td><td class="neg">-28.9</td><td class="neg">-14.9</td><td class="neg">-5.6</td><td>10.4</td><td>24.1</td><td>40.6</td><td>58.1</td><td>199.6</td></tr>
    <tr><td>1 year</td><td>162</td><td class="neg">-25.7</td><td>12.2</td><td>36.7</td><td>78.8</td><td>138</td><td>218</td><td>301</td><td>1,046</td></tr>
    <tr><td>3 year</td><td>6,109</td><td class="neg">-11.4</td><td>290</td><td>608</td><td>1,640</td><td>3,612</td><td>7,540</td><td>13,210</td><td>198,433</td></tr>
    <tr><td>5 year</td><td>96,093</td><td>48.2</td><td>1,604</td><td>4,412</td><td>17,902</td><td>51,380</td><td>120,441</td><td>233,950</td><td>3,901,002</td></tr>
  </table>
  <p class="body-text" style="left:20px;top:88px;width:218px;font-size:4.6px">Assumes 5% price discount per trade and liquid markets. The table shows returns expressed as a percentage of the initial investment, by the amount of time since the investment period began. Each row shows estimated returns distributions using Monte Carlo simulation and bootstrapping methods. The estimates are drawn from simulated samples containing 10,000 observations for each return. The simulated returns do not account for fees and taxes, which may reduce an investor's actual returns.</p>
  <div class="footer"></div>
</section>

<section class="slide" style="left:895px;top:60px">
  <h2 class="slide-title">Actual Performance</h2><div class="slide-rule"></div>
  <p class="body-text" style="left:20px;top:70px;width:70px;font-size:5px">The fund will launch in May 2016.<br><br>We will report fund performance on a monthly basis starting in June.</p>
  <div class="photo" role="img" aria-label="Green-tinted city skyline with rising market chart" style="left:96px;top:33px;width:142px;height:146px;background:linear-gradient(160deg,#3f9a6c,#6fc49a 50%,#2a7a52)"></div>
  <p style="position:absolute;left:125px;top:74px;font-size:28px;font-weight:700;color:#fff">2016</p>
  <div class="footer"></div>
</section>

<!-- Row 2 -->
<section class="slide" style="left:52px;top:280px">
  <h2 class="slide-title">Investment Objective</h2><div class="slide-rule"></div>
  <ul class="objectives">
    <li>Profit from inefficiencies in equity and index options markets<br>&nbsp;-Buy options that are underpriced<br>&nbsp;-Sell options that are overpriced</li>
    <li>Achieve outsized and consistent returns by maintaining a small and nimble fund that can exploit price inefficiencies and move in and out of trades quickly</li>
  </ul>
  <div class="photo" role="img" aria-label="Green rising bar chart with upward arrow illustration" style="left:122px;top:27px;width:118px;height:152px;background:linear-gradient(150deg,#0f5a34,#3aa06a 55%,#0f4a2c)"></div>
  <div class="footer"></div>
</section>

<section class="slide" style="left:333px;top:280px">
  <h2 class="slide-title">Simulated Performance</h2><div class="slide-rule"></div>
  <svg class="chart" viewBox="0 0 214 75" aria-label="Simulated return distribution chart">
    <rect width="214" height="75" fill="#1f6a42"/>
    <text x="107" y="6" font-size="3" fill="#cfe8d8" text-anchor="middle" font-family="Arimo">under a more conservative assumed price discount premium (5%)</text>
    <rect x="18" y="10" width="178" height="52" fill="none" stroke="#9ccfb2" stroke-width=".5"/>
    <path d="M20 60 C40 58 55 30 75 24 C90 20 95 40 110 52 C130 60 160 61 194 61" fill="none" stroke="#e4f2ea" stroke-width=".8"/>
    <path d="M20 60 C50 60 70 56 90 40 C110 22 130 14 194 13" fill="none" stroke="#e4f2ea" stroke-width=".8"/>
    <line x1="150" y1="68" x2="158" y2="68" stroke="#e4f2ea" stroke-width=".6"/>
    <text x="160" y="69" font-size="2.6" fill="#e4f2ea" font-family="Arimo">density</text>
    <line x1="174" y1="68" x2="182" y2="68" stroke="#e4f2ea" stroke-width=".6"/>
    <text x="184" y="69" font-size="2.6" fill="#e4f2ea" font-family="Arimo">cdf</text>
  </svg>
  <p class="body-text" style="left:36px;top:122px;width:200px;font-size:5px">Mean simulated annual return is 162%<br>Only 1% of simulated annual returns are lower than 25.7%<br>The mean 3-year and 5-year simulated returns are 6,109% and 96,093%.<br>The worst simulated 3-year return out of 10,000 simulated observations is +8%.<br>The worst simulated 5-year return out of 10,000 simulated observations is +1,048%.</p>
  <div class="footer"></div>
</section>

<section class="slide" style="left:614px;top:280px">
  <h2 class="slide-title">Risk Management</h2><div class="slide-rule"></div>
  <div class="risk-row" style="top:36px"><div class="risk-icon"><svg viewBox="0 0 22 22" width="18" height="18"><path d="M5 10 L9 14 L15 6" fill="none" stroke="#fff" stroke-width="2.4"/></svg></div><div class="risk-note">Our top priority is safety</div></div>
  <div class="risk-row" style="top:68px"><div class="risk-icon"></div><div class="risk-note">If the market does not offer a price discount or premium, we trade at the best available price to stay within our trading parameters.</div></div>
  <div class="risk-row" style="top:104px"><div class="risk-icon" style="background:#fff;border-color:#5aa532"><svg viewBox="0 0 22 22" width="18" height="18"><text x="9" y="15" font-size="13" fill="#5aa532" text-anchor="middle" font-family="Arimo">$</text></svg></div><div class="risk-note">This approach minimizes losses in illiquid markets.</div></div>
  <div class="risk-row" style="top:136px"><div class="risk-icon"></div><div class="risk-note" style="font-size:3.4px">The simulated strategy performance at substantially lower average price discount premiums, relative to the averages we have achieved to date, exhibits limited downside risk (see simulation results at 5% versus 8% discount premium).</div></div>
  <div class="footer"></div>
</section>

<section class="slide" style="left:895px;top:280px">
  <h2 class="slide-title">Manager Bios</h2><div class="slide-rule"></div>
  <div class="footer"></div>
</section>

<!-- Row 3 -->
<section class="slide" style="left:52px;top:502px">
  <h2 class="slide-title">Simulated Performance</h2><div class="slide-rule"></div>
  <table class="perf-table">
    <tr><th>period</th><th>mean</th><th>1%</th><th>5%</th><th>10%</th><th>25%</th><th>50%</th><th>75%</th><th>90%</th><th>max</th></tr>
    <tr><td>weekly</td><td>1.4</td><td class="neg">-12.9</td><td class="neg">-6.8</td><td class="neg">-4.4</td><td>0.0</td><td>1.5</td><td>3.6</td><td>6.5</td><td>29.8</td></tr>
    <tr><td>monthly</td><td>6.1</td><td class="neg">-24.7</td><td class="neg">-13.2</td><td class="neg">-7.9</td><td>0.4</td><td>5.8</td><td>12.4</td><td>20.3</td><td>79.2</td></tr>
    <tr><td>quarterly</td><td>17.9</td><td class="neg">-33.1</td><td class="neg">-18.6</td><td class="neg">-10.2</td><td>4.1</td><td>16.2</td><td>30.2</td><td>46.5</td><td>171.3</td></tr>
    <tr><td>1 year</td><td>129</td><td class="neg">-29.5</td><td class="neg">-2.1</td><td>18.4</td><td>51.9</td><td>104</td><td>176</td><td>251</td><td>912</td></tr>
    <tr><td>3 year</td><td>3,129</td><td class="neg">-21.8</td><td>129</td><td>302</td><td>880</td><td>2,004</td><td>4,116</td><td>7,302</td><td>101,556</td></tr>
    <tr><td>5 year</td><td>6,759</td><td>216</td><td>588</td><td>1,210</td><td>3,404</td><td>9,850</td><td>21,330</td><td>40,118</td><td>902,114</td></tr>
  </table>
  <p class="body-text" style="left:20px;top:98px;width:218px;font-size:4.6px">Assumes 8% price discount per trade and liquid markets. The table shows returns expressed as a percentage of the initial investment, by the amount of time since the investment period began. Each row shows estimated returns distributions using Monte Carlo simulation and bootstrapping methods. The estimates are drawn from simulated samples containing 10,000 observations for each return. The simulated returns do not account for fees and taxes, which may reduce an investor's actual returns.</p>
  <div class="footer"></div>
</section>

<section class="slide" style="left:333px;top:502px">
  <h2 class="slide-title">Simulated Performance</h2><div class="slide-rule"></div>
  <svg class="chart" viewBox="0 0 214 75" aria-label="Simulated return distribution chart">
    <rect width="214" height="75" fill="#1f6a42"/>
    <text x="107" y="6" font-size="3" fill="#cfe8d8" text-anchor="middle" font-family="Arimo">under a more conservative assumed price discount premium (8%)</text>
    <rect x="18" y="10" width="178" height="52" fill="none" stroke="#9ccfb2" stroke-width=".5"/>
    <path d="M20 60 C30 40 40 14 55 14 C75 14 100 40 130 54 C150 60 170 61 194 61" fill="none" stroke="#e4f2ea" stroke-width=".8"/>
    <path d="M20 60 C40 58 60 40 80 30 C110 16 140 13 194 12" fill="none" stroke="#e4f2ea" stroke-width=".8"/>
    <line x1="150" y1="68" x2="158" y2="68" stroke="#e4f2ea" stroke-width=".6"/>
    <text x="160" y="69" font-size="2.6" fill="#e4f2ea" font-family="Arimo">density</text>
    <line x1="174" y1="68" x2="182" y2="68" stroke="#e4f2ea" stroke-width=".6"/>
    <text x="184" y="69" font-size="2.6" fill="#e4f2ea" font-family="Arimo">cdf</text>
  </svg>
  <p class="body-text" style="left:36px;top:122px;width:200px;font-size:5px">Mean simulated annual return is 129%<br>1% of the time, annual simulated returns are lower than -29.5%<br>The mean 3-year and 5-year simulated returns are 3,129% and 6,759%.<br>Only 1% of 5-year returns fall below +216%<br>The worst simulated 5-year return out of 10,000 simulated observations is -16%.</p>
  <div class="footer"></div>
</section>

<section class="slide" style="left:614px;top:502px">
  <h2 class="slide-title">Key Investment Terms</h2><div class="slide-rule"></div>
  <table class="terms">
    <tr><th>Fund</th><th>Quellmore Derivatives Fund LP</th></tr>
    <tr><td>Management Company</td><td>Quellmore Capital Management LLC</td></tr>
    <tr><td>Eligible Investors</td><td>Qualified Clients</td></tr>
    <tr><td>Minimum Initial Investment</td><td>$50,000</td></tr>
    <tr><td>Additional Contributions</td><td>Monthly on 1st of month, min $10,000</td></tr>
    <tr><td>Redemptions</td><td>Monthly with 10 day notice</td></tr>
    <tr><td>Lock-up period</td><td>none</td></tr>
    <tr><td>Management Fee</td><td>2%</td></tr>
    <tr><td>Performance Fee</td><td>20%</td></tr>
    <tr><td>Legal Counsel</td><td>Pellwick Tanner LLP</td></tr>
    <tr><td>Administrator</td><td>Orrindale Fund Services LLC</td></tr>
    <tr><td>Auditor</td><td>To be determined</td></tr>
    <tr><td>Prime Broker</td><td>Brackwater Prime LLC</td></tr>
  </table>
  <div class="footer"></div>
</section>

<section class="slide" style="left:895px;top:502px">
  <h2 class="slide-title">Contact Information</h2><div class="slide-rule"></div>
  <div class="photo" role="img" aria-label="Hand touching a glowing email icon on a light blue screen" style="left:20px;top:34px;width:208px;height:134px;background:linear-gradient(135deg,#d9eef5,#bfe1ee 50%,#e9f4f8)"></div>
  <p class="wordmark" style="position:absolute;left:174px;top:150px">Quellmore</p>
  <div class="footer"></div>
</section>

</body>
</html>
```